Grain Clear Kitchen Web Design

We are looking for designs for a homepage for a gluten free, health food website.

We are looking for the site to be a shop, as well as a resource/information source for users. We will also look to incorporate recipes, blogs, forums and potentially some other useful information.

We want to ensure that the website is user-friendly, does not have a corporate feel, but is still classy.

We want to have high quality photographic images in the background, with text in the foreground - but these things will need to compliment each other well. e.g recipe of the week integrated onto the background photo and the 'shop' in the foreground.

We have seen a site that we quite like and although we like the design, we do not want to completely emulate this. However, it is a useful starting point for designers and perhaps some inspiration www.brightpantryhall.example

We already have a logo - see attached - which will need to be fully integrated into the design.

We do want a colourful design, but mainly in terms of the images rather than the graphics.
Updates

Please note:

We are pleased with the designs to date, for the most part. We would like you all to note, however, that we are much preferring the lighter designs - ones that make the sites feel brighter - rather than those which are darker in appearance.

We would also like to see less space allocated to the main image, within the context of the site as a whole.

Thanks.

We have eliminated those which we feel are not what we are looking for. We are still keen to see some more designs and are still looking for something unique. There are some good things in all of the designs that we have not eliminated, however we still feel there is room for more inspiration.

Thanks.

Target Market(s)

Our audience are body conscience people looking for health food products. They are also those who are potentially looking for a new lifestyle/life cha

Industry/Entity Type

Health

Requirements
Must have
• Our logo - attached, can provide variations in due course.

Navigational features as per mock up attached.

Social network integration.

NB: we only need one (home) page for this.

```html
<!DOCTYPE html>
<html lang="en">
<head>
<meta charset="utf-8">
<title>Grain Clear Kitchen</title>
<link rel="stylesheet" href="https://fonts.googleapis.com/css2?family=Open+Sans:wght@300;400;600&display=swap">
<style>
:root{
  --wood-dark:#4a2614;
  --wood-mid:#7a4527;
  --wood-light:#9a5c35;
  --header-bg:#efefef;
  --ink:#444;
  --ink-soft:#666;
  --red:#8c1f24;
  --red-deep:#6e161a;
  --green:#62b82c;
  --green-deep:#4c9a1e;
  --blue:#2a8db3;
  --blue-deep:#1f7396;
  --charcoal:#3c3c3c;
  --paper:#fff;
  --footer:#232323;
  --footer-line:#3a3a3a;
  --footer-bottom:#161616;
}
*{box-sizing:border-box;margin:0;padding:0}
html,body{width:1200px;height:976px;overflow:hidden}
body{font-family:"Open Sans",Arial,sans-serif;color:var(--ink);position:relative;background:var(--wood-mid)}
a{color:inherit;text-decoration:none}

.wood-backdrop{position:absolute;left:0;top:0;width:1200px;height:741px;
  background:linear-gradient(90deg,var(--wood-dark) 0%,var(--wood-mid) 18%,var(--wood-light) 45%,var(--wood-mid) 75%,var(--wood-dark) 100%)}

/* header */
.site-header{position:absolute;left:0;top:9px;width:1200px;height:82px;background:var(--header-bg);border-top:1px solid #d5d5d5}
.brand{position:absolute;left:222px;top:18px;display:flex;align-items:center;gap:10px}
.brand-dot{width:28px;height:28px;border-radius:50%;background:var(--charcoal)}
.brand-name{font-size:20px;font-weight:600;color:var(--charcoal)}
.basket{position:absolute;left:547px;top:7px;width:182px;height:27px;border:1px solid var(--red);display:flex;font-size:11px}
.basket-count{flex:1;background:#fff;color:var(--red);text-align:center;line-height:25px}
.basket-label{width:79px;background:var(--red);color:#fff;text-align:center;line-height:25px;font-size:13px}
.account-btn{position:absolute;top:7px;height:27px;background:#1b1b1b;color:#fff;font-size:13px;text-align:center;line-height:27px}
.btn-login{left:737px;width:70px;font-size:14px}
.btn-register{left:813px;width:70px}
.search{position:absolute;left:891px;top:7px;width:166px;height:27px;border:1px solid var(--green);background:#fff;display:flex}
.search-input{flex:1;font-size:10px;font-style:italic;color:var(--green);padding-left:11px;line-height:25px}
.search-btn{width:30px;background:var(--green);display:flex;align-items:center;justify-content:center}
.main-nav{position:absolute;right:149px;top:50px;display:flex;font-size:13px;color:#555}
.main-nav a{padding:0 10px;border-left:1px solid #aaa;line-height:14px}
.main-nav a:first-child{border-left:0}
.main-nav a:last-child{padding-right:0}

.welcome{position:absolute;left:413px;top:123px;width:594px;height:40px;background:#3e3e3e;color:#fff;font-size:16px;text-align:center;line-height:40px;white-space:nowrap;box-shadow:0 3px 6px rgba(0,0,0,.4)}

/* cards */
.card{position:absolute;background:var(--paper);border:2px solid #fff;box-shadow:0 2px 6px rgba(0,0,0,.4)}
.card-title{height:37px;color:#fff;font-size:18px;font-weight:300;line-height:37px;padding-left:18px;position:relative;white-space:nowrap}
.share-icon{position:absolute;right:8px;top:6px}
.body-text{font-size:10.5px;line-height:16px;color:var(--ink-soft)}
.more{color:var(--blue)}

.about{left:163px;top:201px;width:208px;height:138px}
.about .card-title{background:#444;text-align:center;padding:0;font-size:17px}
.about .body-text{padding:8px 12px}

.side-btn{position:absolute;left:163px;width:207px;height:31px;color:#fff;font-size:17px;font-weight:300;line-height:30px;padding-left:14px;border:1px solid #fff;box-shadow:0 2px 4px rgba(0,0,0,.4)}
.side-btn.posts{top:344px;background:var(--blue)}
.side-btn.recipes{top:381px;background:var(--green)}
.side-btn.shop{top:419px;background:var(--red)}

.recipe{left:384px;top:202px;width:423px;height:249px}
.recipe .card-title{background:var(--red);font-size:19px;padding-left:20px}
.recipe-photo{position:absolute;left:11px;top:48px;width:208px;height:133px;background:radial-gradient(circle at 50% 45%,#f3e3c2 0%,#d9b98a 45%,#9a3a2c 70%,#ece9e4 100%)}
.thumb{position:absolute;top:190px;width:64px;height:42px;border:1px solid #ccc}
.thumb-1{left:11px;background:linear-gradient(#5a3326,#2e1a12)}
.thumb-2{left:83px;background:linear-gradient(#f3dde2,#c8d7e4)}
.thumb-3{left:155px;background:linear-gradient(#d8b98a,#3c4a86)}
.recipe-copy{position:absolute;left:234px;top:42px;width:185px}
.recipe-copy h3{font-size:16px;font-weight:400;color:#444;margin-bottom:9px}
.recipe-copy p+p{margin-top:10px}
.full-recipe{position:absolute;left:234px;top:214px;width:194px;height:25px;background:#3c3c3c;color:#fff;font-size:12px;line-height:25px;padding-left:14px}
.full-recipe svg{position:absolute;right:7px;top:7px}

.latest{left:823px;top:203px;width:241px;height:248px}
.latest .card-title{background:var(--blue);text-align:center;padding:0;font-size:18px}
.post-date{position:absolute;left:8px;top:46px;color:var(--blue);font-size:25px;font-weight:300;line-height:26px}
.post-date small{display:block;font-size:8px;line-height:10px;padding-left:2px}
.post-title{position:absolute;left:52px;top:58px;font-size:15.5px;font-weight:400;line-height:20px;white-space:nowrap;color:#444}
.latest .body-text{position:absolute;left:8px;top:91px;width:226px;font-size:10px;line-height:15.5px}
.post-meta{position:absolute;left:8px;top:184px;width:226px;font-size:9.5px;display:flex;justify-content:space-between}
.post-meta em{font-style:normal;color:var(--blue)}
.post-meta b{font-weight:600}
.blog-tab{position:absolute;left:0;bottom:0;width:74px;height:30px;background:#bfe0ec;color:var(--blue);font-size:13px;text-align:center;line-height:30px}
.view-posts{position:absolute;right:40px;bottom:8px;color:var(--blue);font-size:12.5px}
.corner{position:absolute;right:0;bottom:0}

/* products */
.product{position:absolute;top:477px;width:165px;height:211px;background:#fff;border:2px solid #fff;box-shadow:0 2px 6px rgba(0,0,0,.4)}
.product-name{height:32px;background:var(--green);color:#fff;font-size:15px;font-weight:300;text-align:center;line-height:32px}
.product-photo{height:143px;margin:0}
.product-foot{position:absolute;left:0;bottom:0;width:161px;height:32px;display:flex}
.price{width:75px;background:#d6ecc6;color:var(--green-deep);font-size:15px;line-height:32px;text-align:center}
.add{flex:1;font-size:13px;line-height:32px;padding-left:14px;color:#555;background:#fff;position:relative}
.add .corner{right:0;bottom:0}
.p1{left:163px}.p2{left:348px}.p3{left:533px}.p4{left:717px}.p5{left:900px}
.ph-crackers{background:radial-gradient(circle at 55% 50%,#e7b46a 0%,#f4ecd9 55%,#fff 80%)}
.ph-pretzels{background:linear-gradient(160deg,#f2a23c,#e0641f 55%,#a3461a)}
.ph-bread{background:linear-gradient(90deg,#c9b08a,#e8dcc3 30%,#c7a777 50%,#e8dcc3 70%,#bfa27a)}
.ph-pasta{background:linear-gradient(160deg,#d93c24,#f2c14b 40%,#2f5a2e 70%,#e8ddc8)}

/* footer */
.site-footer{position:absolute;left:0;top:741px;width:1200px;height:199px;background:var(--footer);color:#ddd}
.foot-col{position:absolute;top:11px}
.foot-col h4{font-size:14px;font-weight:600;color:#fff;margin-bottom:14px}
.foot-links{list-style:none;width:207px;font-size:10.5px}
.foot-links li{height:27px;line-height:26px;border-bottom:1px solid var(--footer-line);padding-left:8px}
.col-links{left:163px;top:12px}
.col-newsletter{left:391px}
.col-account{left:617px;top:12px}
.col-contact{left:849px}
.col-newsletter p{width:185px;font-size:10.5px;line-height:17.5px;margin-top:-4px}
.signup{margin-top:7px;width:192px;height:34px;border:2px solid var(--green);display:flex;background:#fff}
.signup span{flex:1}
.signup i{width:33px;background:var(--green);display:flex;align-items:center;justify-content:center}
.col-contact address{font-style:normal;font-size:10.5px;line-height:18px}
.col-contact .mail{color:var(--green)}
.social{display:flex;gap:6px;margin-top:9px}
.social span{width:26px;height:26px;border-radius:3px}
.s1{background:#2aa3d8}.s2{background:#3b5a98}.s3{background:#d1402e}.s4{background:#c8232c}
.legal{position:absolute;left:0;top:940px;width:1200px;height:36px;background:var(--footer-bottom);color:#bbb;font-size:9.5px;line-height:36px;padding-left:265px}
</style>
</head>
<body>
<div class="wood-backdrop" role="img" aria-label="Background photograph of warm brown wooden planks"></div>

<header class="site-header">
  <a class="brand" href="#"><span class="brand-dot"></span><span class="brand-name">Grain Clear Kitchen</span></a>
  <div class="basket"><span class="basket-count">0 Item(s) in</span><span class="basket-label">Basket</span></div>
  <a class="account-btn btn-login" href="#">Login</a>
  <a class="account-btn btn-register" href="#">Register</a>
  <div class="search"><span class="search-input">Product search.....</span>
    <span class="search-btn"><svg width="14" height="14" viewBox="0 0 14 14"><circle cx="6" cy="6" r="4.2" fill="none" stroke="#fff" stroke-width="2"/><line x1="9" y1="9" x2="13" y2="13" stroke="#fff" stroke-width="2.4"/></svg></span></div>
  <nav class="main-nav"><a href="#">Shop</a><a href="#">Our Story</a><a href="#">Hints &amp; tips</a><a href="#">Recipes</a><a href="#">Blog</a><a href="#">Contact</a></nav>
</header>

<div class="welcome">Welcome to Grain Clear Kitchen - The one stop shop for everthing Gluten Free</div>

<section class="card about">
  <h2 class="card-title">Grain Clear Kitchen</h2>
  <p class="body-text">Ut scelerisque diam. Donec pulvinar ultricies sem, vel dapibus eros Maecenas auctor.Ut scelerisque diam. Donec pulvinar ultricies sem, vel dapibus eros Maecenas auctor.</p>
</section>
<a class="side-btn posts" href="#">Latest Posts</a>
<a class="side-btn recipes" href="#">View all Recipes</a>
<a class="side-btn shop" href="#">Go to the Shop</a>

<section class="card recipe">
  <h2 class="card-title">New York baked cheesecake
    <svg class="share-icon" width="12" height="11" viewBox="0 0 12 11"><path d="M1 3v7h9V7" fill="none" stroke="#fff" stroke-width="1.4"/><path d="M5 6l6-5M7 1h4v4" fill="none" stroke="#fff" stroke-width="1.4"/></svg></h2>
  <div class="recipe-photo" role="img" aria-label="Photo of a baked cheesecake with strawberry topping, a slice cut out"></div>
  <div class="thumb thumb-1" role="img" aria-label="Thumbnail of a chocolate cake"></div>
  <div class="thumb thumb-2" role="img" aria-label="Thumbnail of pastel cupcakes"></div>
  <div class="thumb thumb-3" role="img" aria-label="Thumbnail of blueberry muffins"></div>
  <div class="recipe-copy">
    <h3>Ut scelerisque diam.</h3>
    <p class="body-text">Donec pulvinar ultricies sem, vel dapibus eros Maecenas auctor.Ut scelerisque diam. Donec pulvinar ultricies sem, vel dapibus eros Maecenas auctor.</p>
    <p class="body-text">Ut scelerisque diam. Donec pulvinar ultricies sem, vel dapibus <span class="more">more...</span></p>
  </div>
  <a class="full-recipe" href="#">Full&nbsp; Recipe
    <svg width="10" height="10" viewBox="0 0 10 10"><circle cx="4" cy="4" r="3" fill="none" stroke="#fff" stroke-width="1.4"/><line x1="6.2" y1="6.2" x2="9" y2="9" stroke="#fff" stroke-width="1.6"/></svg></a>
</section>

<section class="card latest">
  <h2 class="card-title">Latest Posts
    <svg class="share-icon" width="12" height="11" viewBox="0 0 12 11"><path d="M1 3v7h9V7" fill="none" stroke="#fff" stroke-width="1.4"/><path d="M5 6l6-5M7 1h4v4" fill="none" stroke="#fff" stroke-width="1.4"/></svg></h2>
  <div class="post-date">04<small>Jan 11</small></div>
  <h3 class="post-title">Donec pulvinar ultricies</h3>
  <p class="body-text">vel dapibus eros Maecenas auctor quam sit amet ante tristique sodales.vel dapibus eros Maecenas auctor quam sit amet ante. &nbsp;tristique sodales.vel dapibus eros Maecenas auctor quam sit amet ante <span class="more">more...</span></p>
  <div class="post-meta"><span>Tags: <em>Latest new, Gluten free</em></span><b>- Ada Penrose</b></div>
  <a class="blog-tab" href="#">Blog</a>
  <a class="view-posts" href="#">View all posts</a>
  <svg class="corner" width="34" height="34" viewBox="0 0 34 34"><path d="M34 0V34H0Z" fill="var(--blue)"/><circle cx="23" cy="22" r="3.4" fill="none" stroke="#fff" stroke-width="1.4"/><line x1="25.5" y1="24.5" x2="29" y2="28" stroke="#fff" stroke-width="1.6"/></svg>
</section>

<article class="product p1"><h3 class="product-name">Product Name</h3>
  <div class="product-photo ph-crackers" role="img" aria-label="Product photo of a box of gluten free oat crackers"></div>
  <div class="product-foot"><span class="price">£ 0.50</span><span class="add">Add to<svg class="corner" width="30" height="30" viewBox="0 0 30 30"><path d="M30 0V30H0Z" fill="var(--green)"/><path d="M21 22h6M24 19v6" stroke="#fff" stroke-width="1.6"/></svg></span></div></article>
<article class="product p2"><h3 class="product-name">Product Name</h3>
  <div class="product-photo ph-pretzels" role="img" aria-label="Product photo of a bag of gluten free pretzels"></div>
  <div class="product-foot"><span class="price">£ 2.50</span><span class="add">Add to<svg class="corner" width="30" height="30" viewBox="0 0 30 30"><path d="M30 0V30H0Z" fill="var(--green)"/><path d="M21 22h6M24 19v6" stroke="#fff" stroke-width="1.6"/></svg></span></div></article>
<article class="product p3"><h3 class="product-name">Product Name</h3>
  <div class="product-photo ph-bread" role="img" aria-label="Product photo of two wrapped gluten free loaves"></div>
  <div class="product-foot"><span class="price">£ 5.50</span><span class="add">Add to<svg class="corner" width="30" height="30" viewBox="0 0 30 30"><path d="M30 0V30H0Z" fill="var(--green)"/><path d="M21 22h6M24 19v6" stroke="#fff" stroke-width="1.6"/></svg></span></div></article>
<article class="product p4"><h3 class="product-name">Product Name</h3>
  <div class="product-photo ph-pasta" role="img" aria-label="Product photo of a pack of gluten free pasta with tomatoes"></div>
  <div class="product-foot"><span class="price">£ 4.98</span><span class="add">Add to<svg class="corner" width="30" height="30" viewBox="0 0 30 30"><path d="M30 0V30H0Z" fill="var(--green)"/><path d="M21 22h6M24 19v6" stroke="#fff" stroke-width="1.6"/></svg></span></div></article>
<article class="product p5"><h3 class="product-name">Product Name</h3>
  <div class="product-photo ph-bread" role="img" aria-label="Product photo of two wrapped gluten free loaves"></div>
  <div class="product-foot"><span class="price">£ 2.50</span><span class="add">Add to<svg class="corner" width="30" height="30" viewBox="0 0 30 30"><path d="M30 0V30H0Z" fill="var(--green)"/><path d="M21 22h6M24 19v6" stroke="#fff" stroke-width="1.6"/></svg></span></div></article>

<footer class="site-footer">
  <div class="foot-col col-links"><h4>Useful links</h4>
    <ul class="foot-links"><li>Contact us</li><li>FAQs</li><li>Site Map</li><li>Privacy Policy</li></ul></div>
  <div class="foot-col col-newsletter"><h4>Newsletter sign up</h4>
    <p>To keep upto date with the latest news and information about our services please fill out your Email address below:</p>
    <div class="signup"><span></span><i><svg width="18" height="18" viewBox="0 0 18 18"><circle cx="9" cy="9" r="7.5" fill="none" stroke="#fff" stroke-width="1.4"/><path d="M5 9h7M9 6l3 3-3 3" fill="none" stroke="#fff" stroke-width="1.4"/></svg></i></div></div>
  <div class="foot-col col-account"><h4>Your account</h4>
    <ul class="foot-links"><li>Create Account</li><li>Sign In</li><li>Shopping basket</li><li>Store Locations</li><li>Customer Service</li></ul></div>
  <div class="foot-col col-contact"><h4>Stay in touch</h4>
    <address>24 Millbrook Lane,<br>Harwick,<br>Westshire , HK4 2RN<br>+44(0) 0000 111 222<br><span class="mail">hello@grainclear.example</span></address>
    <div class="social"><span class="s1"></span><span class="s2"></span><span class="s3"></span><span class="s4"></span></div></div>
</footer>
<div class="legal">Copyright © 2013 Studio Larch. Use of this website constitutes acceptance of our User Agreement and Privacy Policy.</div>
</body>
</html>
```